Qolvar Energy Information Site Redesign

Re-vamp current site at qolvarenergy.com to include new logo, verbiage updates as needed, redesign, etc. Company overview and additional information on current QVR url.

```html
<!DOCTYPE html>
<html lang="en">
<head>
<meta charset="utf-8">
<title>Qolvar Energy Information</title>
<link href="https://fonts.googleapis.com/css2?family=Roboto:ital,wght@0,300;0,400;0,500;0,700;1,300;1,400&display=swap" rel="stylesheet">
<style>
:root{
  --orange:#e8892b;
  --orange-light:#f2a857;
  --ink:#222;
  --text:#444;
  --muted:#666;
  --grey-bg:#efefef;
  --white:#fff;
  --dark:#2f2f2f;
  --panel:#e4e4e4;
  --blue:#2a6fa8;
}
*{box-sizing:border-box;margin:0;padding:0}
html,body{width:1200px;height:2550px;overflow:hidden}
body{font-family:'Roboto',sans-serif;color:var(--text);background:var(--white);position:relative}
.section{position:absolute;left:0;width:1200px}
.section-title{position:absolute;left:0;width:1200px;text-align:center;font-size:29px;font-weight:400;color:var(--ink)}
.section-title::after{content:"";display:block;width:64px;height:3px;background:var(--orange);margin:12px auto 0}
.btn{position:absolute;border:2px solid var(--orange);color:var(--orange);font-size:11px;letter-spacing:1px;text-transform:uppercase;display:flex;align-items:center;justify-content:center;background:transparent}

/* hero */
.hero{top:0;height:450px;background:linear-gradient(180deg,#141820 0%,#3a3340 45%,#5a4330 75%,#8a5a2a 100%)}
.brand{position:absolute;left:240px;top:22px;display:flex;flex-direction:column;align-items:center}
.brand-mark{width:24px;height:24px;border-radius:50%;border:3px solid var(--orange)}
.brand-name{font-size:12px;font-weight:700;color:var(--orange);margin-top:3px;letter-spacing:.5px}
.nav{position:absolute;right:240px;top:38px;display:flex;gap:34px}
.nav a{color:var(--white);font-size:12px;font-weight:500;text-decoration:none}
.hero-lead{position:absolute;left:240px;top:190px;width:740px;color:var(--white);font-size:25px;font-weight:300;font-style:italic;line-height:1.3}

/* about */
.about{top:450px;height:337px;background:var(--grey-bg)}
.about .section-title{top:32px}
.about-text{position:absolute;left:240px;top:100px;width:360px;font-size:13px;line-height:1.6;color:var(--text)}
.about .btn{left:367px;top:240px;width:93px;height:32px}
.about-chart{position:absolute;left:615px;top:104px;width:345px;height:174px;background:linear-gradient(135deg,#3c3f44,#1f2226 60%,#2e3236)}

/* testimonials */
.testimonials{top:787px;height:352px;background:var(--white)}
.testimonials .section-title{top:32px}
.quote-mark{position:absolute;font-size:70px;line-height:1;color:var(--orange);font-weight:700;font-family:Georgia,serif}
.quote-open{left:238px;top:90px}
.quote-close{left:930px;top:140px}
.quote-text{position:absolute;left:304px;top:100px;width:600px;font-size:13px;line-height:1.75;color:var(--text)}
.people{position:absolute;left:395px;top:183px;display:flex;gap:64px}
.person{width:95px;text-align:center}
.avatar{width:95px;height:95px;border-radius:50%;border:3px solid var(--orange);background:linear-gradient(160deg,#d9cbbb,#8c7a6a)}
.person-name{font-size:12.5px;color:var(--text);margin-top:10px}

/* clients */
.clients{top:1139px;height:294px;background:var(--grey-bg)}
.clients .section-title{top:32px}
.client-row{position:absolute;left:238px;top:142px;width:724px;display:flex;justify-content:space-between;align-items:center}
.client{font-size:14px;font-weight:500;color:#333;display:flex;align-items:center;gap:7px}
.client i{display:block;width:12px;height:12px;border-radius:50%;background:var(--orange)}
.clients .btn{left:554px;top:217px;width:93px;height:38px}

/* why us */
.why{top:1433px;height:325px;background:var(--white)}
.why .section-title{top:32px}
.features{position:absolute;left:220px;top:105px;width:760px;display:flex;justify-content:space-between}
.feature{width:145px;text-align:center}
.feature svg{width:46px;height:46px}
.feature-title{font-size:11.5px;font-weight:500;color:var(--ink);margin-top:6px;line-height:1.2;height:30px}
.feature-text{font-size:9.5px;line-height:1.45;color:var(--text);margin-top:8px}

/* contact */
.contact{top:1758px;height:411px;background:linear-gradient(135deg,#6c6460 0%,#4d4743 45%,#5c5652 100%)}
.contact .section-title{top:32px;color:var(--white)}
.contact-intro{position:absolute;left:240px;top:112px;width:300px;color:var(--white)}
.contact-title{font-size:18px;font-weight:400;line-height:1.3}
.contact-lead{font-size:12.5px;line-height:1.3;margin-top:14px}
.contact-line{font-size:12.5px;line-height:1.2}
.contact-company{color:var(--orange);margin-top:16px}
.contact-phone{margin-top:16px}
.contact-email{color:var(--orange)}
.form{position:absolute;left:600px;top:115px;width:361px;height:256px;background:var(--panel);padding:10px 14px}
.form label{display:block;font-size:12px;color:#333}
.field{background:var(--white);border-radius:3px;height:23px;margin:4px 0 14px}
.field.area{height:68px;margin-bottom:12px}
.form .btn{position:static;width:64px;height:24px;font-size:10px}

/* footer */
.footer{top:2169px;height:330px;background:var(--orange-light)}
.footer-brand{position:absolute;left:255px;top:30px;width:110px;display:flex;flex-direction:column;align-items:center}
.footer-brand .brand-mark{width:30px;height:30px}
.footer-brand .brand-name{font-size:16px;color:var(--blue);margin-top:4px}
.follow{position:absolute;left:270px;top:126px;font-size:12.5px;font-weight:500;color:#333}
.socials{position:absolute;left:218px;top:162px;display:flex;gap:9px}
.socials span{width:30px;height:30px;border-radius:50%;background:#333;display:block}
.links-title{position:absolute;left:555px;top:42px;font-size:15px;font-weight:400;color:#333}
.links{position:absolute;left:548px;top:102px;list-style:none}
.links li{font-size:12px;color:#333;height:27px}
.footer-contact{position:absolute;left:770px;top:40px}
.footer-row{display:flex;gap:22px;align-items:flex-start;margin-bottom:32px}
.footer-row svg{width:44px;height:44px}
.footer-row p{font-size:12.5px;line-height:2.1;color:#333}

.copyright{position:absolute;top:2499px;left:0;width:1200px;height:51px;background:var(--dark);color:var(--white);font-size:11px;font-weight:500;display:flex;align-items:center;justify-content:center}
</style>
</head>
<body>

<header class="section hero" role="img" aria-label="Night city skyline with light trails on a busy road">
  <div class="brand"><span class="brand-mark"></span><span class="brand-name">QVR ENERGY</span></div>
  <nav class="nav"><a>What We Do</a><a>Exchange Solutions</a><a>Data Management</a><a>About QVR</a><a>Blog</a></nav>
  <p class="hero-lead">QVR provides the technology to efficiently transfer information electronically and access, integrate and manage data.</p>
</header>

<section class="section about">
  <h2 class="section-title">About Us</h2>
  <p class="about-text">Qolvar Energy Information has been providing electronic exchange solutions for the energy industry for over 20 years. QVR utilizes proven data integration techniques to provide customers with cost effective methods to efficiently access, transform and distribute their data. Our customer list includes over 95% of the Fortune 500 energy companies.</p>
  <span class="btn">Learn More</span>
  <div class="about-chart" role="img" aria-label="Financial trading screen with line charts"></div>
</section>

<section class="section testimonials">
  <h2 class="section-title">Testimonials</h2>
  <span class="quote-mark quote-open">&ldquo;</span>
  <p class="quote-text">Without QVR I would have to hire 2-3 more employees to keep up with the demand of keying lines in. The customer support staff has been GREAT to work with. It's hard to imagine life without QVR. They have certainly made my life easier!</p>
  <span class="quote-mark quote-close">&rdquo;</span>
  <div class="people">
    <div class="person"><div class="avatar" role="img" aria-label="Portrait of John Doe"></div><p class="person-name">John Doe</p></div>
    <div class="person"><div class="avatar" role="img" aria-label="Portrait of Jane Doe"></div><p class="person-name">Jane Doe</p></div>
    <div class="person"><div class="avatar" role="img" aria-label="Portrait of John Smith"></div><p class="person-name">John Smith</p></div>
  </div>
</section>

<section class="section clients">
  <h2 class="section-title">Our Clients</h2>
  <div class="client-row">
    <span class="client"><i></i>Ridgeline Resources</span>
    <span class="client">Summit Petroleum</span>
    <span class="client"><i></i>Mesquite Resources</span>
    <span class="client">Kestrel Energy</span>
    <span class="client">Veranta</span>
  </div>
  <span class="btn">View All</span>
</section>

<section class="section why">
  <h2 class="section-title">Why Us</h2>
  <div class="features">
    <div class="feature">
      <svg viewBox="0 0 46 46" fill="none" stroke="#e8892b" stroke-width="2"><ellipse cx="23" cy="10" rx="14" ry="5"/><path d="M9 10v26c0 3 6 5 14 5s14-2 14-5V10"/><path d="M9 19c0 3 6 5 14 5s14-2 14-5M9 28c0 3 6 5 14 5s14-2 14-5"/></svg>
      <p class="feature-title">Data Management Solutions</p>
      <p class="feature-text">Our data management solutions make it easier for your company to track and manage production and other mission critical business data.</p>
    </div>
    <div class="feature">
      <svg viewBox="0 0 46 46" fill="none" stroke="#e8892b" stroke-width="2"><path d="M13 30h-2a8 8 0 0 1 0-16 11 11 0 0 1 21-2 8 8 0 0 1 3 18h-2"/><path d="M23 42V22M17 28l6-6 6 6"/></svg>
      <p class="feature-title">Well Data Exchange</p>
      <p class="feature-text">Our platform for partner reports, logs, surveys and countless other documents, allows you to outsource time-consuming partner support to QVR.</p>
    </div>
    <div class="feature">
      <svg viewBox="0 0 46 46" fill="none" stroke="#e8892b" stroke-width="2"><rect x="5" y="8" width="36" height="24"/><path d="M17 40h12M23 32v8M12 17h20M28 13l4 4-4 4M34 24H14M18 20l-4 4 4 4"/></svg>
      <p class="feature-title">Partner Data Exchange</p>
      <p class="feature-text">Our exchange solutions enable companies to automatically exchange data which can be integrated into their systems, as well as importing, exporting and distributing the information.</p>
    </div>
    <div class="feature">
      <svg viewBox="0 0 46 46" fill="none" stroke="#e8892b" stroke-width="2"><path d="M9 6h28v34l-4-3-4 3-4-3-4 3-4-3-4 3-4-3z"/><path d="M14 14h6M14 20h6M26 13v14M29 16h-4a2 2 0 0 0 0 4h2a2 2 0 0 1 0 4h-4M14 30h18"/></svg>
      <p class="feature-title">E-Ticket Exchange</p>
      <p class="feature-text">QVR automates the transfer of field tickets between logistics service providers and oil &amp; gas operating companies, including sales runs and water hauls.</p>
    </div>
    <div class="feature">
      <svg viewBox="0 0 46 46" fill="none" stroke="#e8892b" stroke-width="2"><rect x="4" y="16" width="30" height="20" rx="2"/><path d="M10 16l24-8 6 18-6 2M4 22h30M9 30h10"/></svg>
      <p class="feature-title">Owner Relations Services</p>
      <p class="feature-text">With over 85 companies, QVR operates the largest network of internet owner portals in the industry.</p>
    </div>
  </div>
</section>

<section class="section contact" role="img" aria-label="Hands typing on a computer keyboard, darkened backdrop">
  <h2 class="section-title">Contact Us</h2>
  <div class="contact-intro">
    <h3 class="contact-title">If you have a project you would like to discuss, get in touch with us.</h3>
    <p class="contact-lead">Let us know how we can help! QVR Energy provides electronic data exchange and call center solutions to meet your company's business needs.</p>
    <p class="contact-line contact-company">QVR Energy</p>
    <p class="contact-line">450 Cedar Bend Rd.</p>
    <p class="contact-line">Suite 210</p>
    <p class="contact-line">Austin, TX 78700</p>
    <p class="contact-line contact-phone">800-555-0142</p>
    <p class="contact-line contact-email">support@qolvarenergy.com</p>
  </div>
  <div class="form">
    <label>Name</label><div class="field"></div>
    <label>Email</label><div class="field"></div>
    <label>Message</label><div class="field area"></div>
    <span class="btn">Send</span>
  </div>
</section>

<footer class="section footer">
  <div class="footer-brand"><span class="brand-mark"></span><span class="brand-name">QVR ENERGY</span></div>
  <p class="follow">Follow Us On</p>
  <div class="socials" aria-label="Social media links"><span></span><span></span><span></span><span></span><span></span></div>
  <h4 class="links-title">Quick Links</h4>
  <ul class="links"><li>Terms and Conditions</li><li>Privacy Policy</li><li>Site Map</li><li>Offices</li><li>Help</li></ul>
  <div class="footer-contact">
    <div class="footer-row">
      <svg viewBox="0 0 44 44" fill="none" stroke="#2a6fa8" stroke-width="2"><path d="M22 32s-10-10-10-17a10 10 0 0 1 20 0c0 7-10 17-10 17z"/><circle cx="22" cy="15" r="4"/><path d="M14 30l-8 10h32l-8-10"/></svg>
      <p>1740 Harbor Lane,<br>New York, NY 10000</p>
    </div>
    <div class="footer-row">
      <svg viewBox="0 0 44 44" fill="none" stroke="#2a6fa8" stroke-width="2"><path d="M10 6l7 2 2 9-5 3a22 22 0 0 0 10 10l3-5 9 2 2 7-4 4C18 38 6 26 6 10z"/></svg>
      <p>555-0187</p>
    </div>
  </div>
</footer>

<div class="copyright">Copyright QVR Energy | All Rights Reserved</div>

</body>
</html>
```